An insurance broker wants to represent the company's vision visually and textually.

My company, with a total of 10 employees, developed a vision this year. Now, we want to display this vision in the form of a two-meter-high visual that will be mounted on the wall. This ensures that the vision is always visible to our employees, as well as to our clients and partners when they visit our office.

Here's my idea: the vision will be accompanied by a fitting image, with the text of the vision itself elegantly written in a beautiful font. Our vision reads: "Every company always has a perfectly tailored future solution for greater financial security, freedom, and joy."

A bit about my company: we are an insurance broker, and our services are primarily designed for corporate clients.

```html
<!DOCTYPE html>
<html lang="en">
<head>
<meta charset="UTF-8">
<title>Vision – Wall Visual</title>
<link rel="stylesheet" href="https://fonts.googleapis.com/css2?family=Montserrat:wght@500;600&family=Pacifico&display=swap">
<style>
  :root {
    --night: #0a121f;
    --ember: #ff4a0c;
    --copper: #c47a62;
  }
  html, body {
    margin: 0;
    padding: 0;
    overflow: hidden;
    background: var(--night);
  }
  .canvas {
    position: relative;
    width: 1200px;
    height: 1000px;
    background: var(--night);
    overflow: hidden;
  }
  .eclipse {
    position: absolute;
    left: 0;
    top: 0;
  }
  .vision {
    position: absolute;
    right: 385px;
    top: 318px;
    margin: 0;
    text-align: right;
    color: var(--ember);
    font-family: "Montserrat", sans-serif;
    font-weight: 500;
  }
  .vision-line {
    display: block;
    white-space: nowrap;
  }
  .vision-line--small {
    font-size: 31px;
    line-height: 45px;
    letter-spacing: 0.3px;
  }
  .vision-line--bold {
    font-size: 41px;
    line-height: 47px;
    font-weight: 600;
    letter-spacing: 0.6px;
  }
  .vision-script {
    display: block;
    font-family: "Pacifico", cursive;
    font-weight: 400;
    white-space: nowrap;
  }
  .vision-script--freedom {
    font-size: 78px;
    line-height: 100px;
    margin-top: -6px;
    margin-right: -4px;
  }
  .vision-script--closing {
    line-height: 100px;
    margin-right: 2px;
  }
  .vision-script__and {
    font-size: 56px;
  }
  .vision-script__joy {
    font-size: 92px;
  }
</style>
</head>
<body>
  <main class="canvas">
    <svg class="eclipse" width="1200" height="1000" viewBox="0 0 1200 1000" aria-hidden="true">
      <defs>
        <radialGradient id="corona" cx="600" cy="495" r="440" gradientUnits="userSpaceOnUse">
          <stop offset="0" stop-color="#c47a62" stop-opacity="0"/>
          <stop offset="0.735" stop-color="#c47a62" stop-opacity="0"/>
          <stop offset="0.742" stop-color="#c47a62" stop-opacity="0.75"/>
          <stop offset="0.78" stop-color="#c47a62" stop-opacity="0.32"/>
          <stop offset="0.87" stop-color="#c47a62" stop-opacity="0.12"/>
          <stop offset="1" stop-color="#c47a62" stop-opacity="0"/>
        </radialGradient>
      </defs>
      <circle class="eclipse__corona" cx="600" cy="495" r="440" fill="url(#corona)"/>
      <circle class="eclipse__disc" cx="600" cy="495" r="324" fill="#0a121f"/>
    </svg>

    <p class="vision">
      <span class="vision-line vision-line--small">Every company always</span>
      <span class="vision-line vision-line--small">has a perfectly tailored</span>
      <span class="vision-line vision-line--bold">future solution for</span>
      <span class="vision-line vision-line--small">greater financial security,</span>
      <span class="vision-script vision-script--freedom">freedom,</span>
      <span class="vision-script vision-script--closing"><span class="vision-script__and">and </span><span class="vision-script__joy">joy.</span></span>
    </p>
  </main>
</body>
</html>
```